Meridian Rest Supply Needs Business Card

Looking for a very nice looking business card. Creative but not extravagant. We sell beds and pillows across the U.S. and need something professional but catchy. I have attached the logo.

Name : Dale Fenwick
Title : President
Phone : (800) 417-2964
Email: sleep@quorvana.com
Website: www.quorvana.com

Can be single-sided or double-sided
horizontal or vertical

Can use Blues/Greys

Target Market(s)

Mass Market

Industry/Entity Type

Retail

Contact Information for Business Card

Name : Dale Fenwick
Title : President
Phone : (800) 417-2964
Email: sleep@quorvana.com
Website: www.quorvana.com

Requirements
Must have
• Clean, Modern, Smooth
• Can use Blues/Greys
• On the other side without the information - have something simple like www.quorvana.com or our logo
Nice to have
• Surprise me
Should not have
• Nothing crazy, nothing cluttered

```html
<!DOCTYPE html>
<html lang="en">
<head>
<meta charset="utf-8">
<title>Meridian Rest Supply – Business Card</title>
<link rel="stylesheet" href="https://fonts.googleapis.com/css2?family=Arimo:wght@400;700&family=Rokkitt:wght@700&display=swap">
<style>
  :root {
    --backdrop: #cde7df;
    --card: #ffffff;
    --brand-blue: #00aeef;
    --band-blue-deep: #0a86c0;
    --band-blue-light: #25b4e6;
    --bar-grey: #a7a9ac;
    --text-grey: #6d6e71;
    --hairline: #c9cbcd;
  }
  * { margin: 0; padding: 0; box-sizing: border-box; }
  html, body {
    width: 1200px; height: 1200px; overflow: hidden;
    background: var(--backdrop);
  }
  .card {
    position: absolute; left: 100px; top: 314px;
    width: 1000px; height: 571px;
    background: var(--card);
    border-radius: 56px;
    overflow: hidden;
    box-shadow: 0 10px 30px rgba(40, 90, 80, 0.18);
  }
  .brand-name {
    position: absolute; left: 135px; top: 62px;
    font-family: "Arimo", sans-serif; font-weight: 400;
    font-size: 158px; line-height: 1;
    color: var(--brand-blue);
  }
  .tagline {
    position: absolute; right: 150px; top: 232px;
    font-family: "Arimo", sans-serif; font-weight: 400;
    font-size: 27px; letter-spacing: 6px;
    color: var(--text-grey);
  }
  .contact-bar {
    position: absolute; left: 0; width: 611px; height: 38px;
    display: flex; align-items: center;
    font-family: "Arimo", sans-serif; font-size: 28px;
    color: #fff;
  }
  .contact-bar svg { position: absolute; left: 56px; width: 28px; height: 28px; }
  .contact-bar span { position: absolute; left: 99px; }
  .contact-bar.phone { top: 320px; background: var(--bar-grey); }
  .contact-bar.email { top: 370px; background: var(--brand-blue); }
  .contact-bar.web   { top: 422px; background: var(--bar-grey); }
  .person { position: absolute; left: 628px; top: 316px; }
  .person-name {
    font-family: "Rokkitt", serif; font-weight: 700;
    font-size: 47px; line-height: 1; color: var(--brand-blue);
  }
  .person-title {
    font-family: "Arimo", sans-serif; font-size: 26px;
    color: var(--text-grey); margin-top: 2px;
  }
  .web-band {
    position: absolute; left: 0; right: 0; bottom: 0; height: 53px;
    border-top: 3px solid var(--hairline);
    background: linear-gradient(90deg, var(--band-blue-deep) 0%, var(--band-blue-light) 50%, var(--band-blue-deep) 100%);
    display: flex; align-items: center; justify-content: center;
    font-family: "Arimo", sans-serif; font-weight: 700;
    font-size: 37px; color: #fff;
  }
</style>
</head>
<body>
  <main class="card">
    <div class="brand-name">quorvana</div>
    <div class="tagline">BEDS AND PILLOWS</div>

    <div class="contact-bar phone">
      <svg viewBox="0 0 24 24" aria-hidden="true"><path fill="#fff" d="M2 8c0-3 5-5 10-5s10 2 10 5v2h-5V8c-1-1-3-1.5-5-1.5S8 7 7 8v2H2z M6 11h12l2 9H4z"/><circle cx="12" cy="15.5" r="2.6" fill="#a7a9ac"/></svg>
      <span>(800) 417-2964</span>
    </div>
    <div class="contact-bar email">
      <svg viewBox="0 0 24 24" aria-hidden="true"><rect x="2" y="5" width="20" height="14" fill="#fff"/><path d="M2 5l10 8 10-8M2 19l7-7M22 19l-7-7" stroke="#00aeef" stroke-width="1.6" fill="none"/></svg>
      <span>sleep@quorvana.com</span>
    </div>
    <div class="contact-bar web">
      <svg viewBox="0 0 24 24" aria-hidden="true"><g fill="none" stroke="#fff" stroke-width="1.4"><circle cx="12" cy="12" r="9"/><ellipse cx="12" cy="12" rx="4" ry="9"/><path d="M3 12h18M4.5 7.5h15M4.5 16.5h15"/></g></svg>
      <span>www.quorvana.com</span>
    </div>

    <div class="person">
      <div class="person-name">Dale Fenwick</div>
      <div class="person-title">President</div>
    </div>

    <div class="web-band">www.quorvana.com</div>
  </main>
</body>
</html>
```